Design the Mobile Version of Existing Web Based Health Platform

Loomcrest is a social business enterprise that focus on public health by applying innovative healthcare services and consumer internet technology. Loomcrest offers a personalized platform of health promotion and disease prevention that puts the individual back in control of his life.

Loomcrest is looking for a Mobile Web UX/Visual Design professional to create a mobile version of Loomcrest website platform for iPhone, iPad/tablet and Android.

Contestants must to check www.loomcrest-demo.com.br to have a better understanding of Loomcrest Platform by creating an account (it's in portuguese, but anyone can get the general idea).

The mobile version of Loomcrest should have very similar functionality and user flows. This job is not to reengineer or re-imagine Loomcrest. It is just to reformat the existing functionality so it works well on mobile devices.

This description below is to help you to understand the core features of the platform (check the attachments to see the new web design of each one):

- Personally Controlled Health Record - PCHR enables an individual to own and manage a complete, secure, digital copy of her health and wellness information.
- Health Risk Assessments - is a process to estimate the nature and probability of adverse health effects, based on personal and family historical data, behavior and environment.
- Simulation of future health - "what if analysis" that emphasizes health education and behavior change.
- Step Quests - a program that gives you the opportunity to the participant to advance his personal well-being by doing simple Step Quests
- Health Alerts and Recommendations and Missing Data - Recommendations based on Wellbeing Bureau Guidelines and Federal Wellness Review Panel (FWRP), plus notifications to update outdated information.

The deliverable for this project is a psd file with a designed mobile version of Loomcrest.

A new design of the web platform is under construction. You can also check it looking at the files attached.

Target Market(s)

people 25-40 years old, 60% female, socially engaged

Industry/Entity Type

Healthcare

Requirements
Must have
• iPhone, iPad and Android version

Design must cover all current functionalities available on the web version (please, ensure you understand all features by creating an account at www.loomcrest-demo.com.br)

- Login/Sign up
- Welcome (first assessment)
- Add to Personal Controlled Health Record (PCHR)
- Update/Remove PCHR
- List PCHR
- Riskgrid (risk assessmen results)
- Simulation
- Alerts
- Missing data
- Recommendations
- StepQuest
- Badges
- Configurations

It's important to check the attachments to see how the web platform design is evolving.

```html
<!DOCTYPE html>
<html lang="pt">
<head>
<meta charset="utf-8">
<title>Loomcrest – Cadastro</title>
<link href="https://fonts.googleapis.com/css2?family=Questrial&family=Arimo:wght@400;700&family=PT+Sans:wght@400;700&family=Nunito:wght@700;800&display=swap" rel="stylesheet">
<style>
  :root {
    --page-bg: #f2f2f1;
    --brand-orange: #f97a0c;
    --brand-orange-light: #ff9a2a;
    --brand-orange-edge: #d65f00;
    --brand-green: #8dc21f;
    --green-top: #bfe45a;
    --green-bottom: #8fc322;
    --green-edge: #7fb21a;
    --green-label: #4f8a0e;
    --green-note: #1f2a0c;
    --title-grey: #9b9b9b;
    --field-border: #d4d4d4;
    --field-hint: #a3a3a3;
    --social-blue: #3b5a9a;
    --link-blue: #1f4fd6;
    --ink: #333333;
  }
  * { box-sizing: border-box; margin: 0; padding: 0; }
  html, body { width: 948px; height: 1200px; overflow: hidden; }
  body {
    position: relative;
    background: var(--page-bg);
    font-family: "Arimo", Arial, sans-serif;
  }
  .abs { position: absolute; }

  .brand { left: 281px; top: 24px; height: 84px; display: flex; align-items: center; gap: 14px; }
  .brand-mark { width: 84px; height: 74px; background: var(--brand-orange); border-radius: 4px; }
  .brand-name {
    font-family: "Nunito", sans-serif; font-weight: 800; font-size: 72px;
    color: var(--brand-green); letter-spacing: -1px; line-height: 1;
  }
  .brand-rule {
    left: 209px; top: 106px; width: 528px; height: 6px;
    background: radial-gradient(ellipse at center, rgba(0,0,0,.22), rgba(0,0,0,0) 70%);
  }
  .tagline {
    left: 0; width: 948px; top: 148px; text-align: center;
    font-family: "Questrial", sans-serif; font-size: 48px; font-weight: 700;
    color: var(--title-grey); letter-spacing: 1px;
  }

  .social-signup {
    left: 191px; top: 219px; width: 540px; height: 52px;
    border-radius: 14px; overflow: hidden; display: flex;
    border: 1px solid var(--brand-orange-edge);
    box-shadow: 0 2px 3px rgba(0,0,0,.15);
  }
  .social-signup .network-tab { width: 60px; background: var(--social-blue); }
  .social-signup .label {
    flex: 1; display: flex; align-items: center; justify-content: center;
    background: linear-gradient(var(--brand-orange-light), var(--brand-orange));
    color: #fff; font-family: "Questrial", sans-serif; font-weight: 700; font-size: 28px;
  }

  .field {
    left: 217px; width: 485px; height: 48px; background: #fff;
    border: 1px solid var(--field-border);
    padding-left: 21px; display: flex; align-items: center;
    color: var(--field-hint); font-size: 17px;
  }
  .terms { left: 222px; top: 483px; display: flex; align-items: center; gap: 10px; font-size: 13px; color: var(--ink); }
  .terms .box { width: 20px; height: 20px; background: #fff; border: 1px solid #c8c8c8; }
  .terms a { color: var(--link-blue); text-decoration: none; }

  .signup-button {
    left: 215px; top: 538px; width: 488px; height: 50px; border-radius: 25px;
    background: var(--brand-orange); border: 1px solid var(--brand-orange-edge);
    display: flex; align-items: center; justify-content: center;
    color: #fff; font-family: "Questrial", sans-serif; font-weight: 700; font-size: 28px;
  }

  .menu-pill {
    height: 56px; border-radius: 28px;
    background: linear-gradient(var(--green-top), var(--green-bottom));
    border: 1px solid var(--green-edge);
    display: flex; align-items: center; padding-left: 14px; gap: 10px;
    box-shadow: inset 0 1px 0 rgba(255,255,255,.5), 0 1px 2px rgba(0,0,0,.12);
    white-space: nowrap;
  }
  .menu-pill svg { width: 34px; height: 34px; flex: none; }
  .menu-pill .title { font-family: "Questrial", sans-serif; font-size: 30px; color: var(--green-label); text-shadow: 0 1px 0 rgba(255,255,255,.45); }
  .menu-pill .note { font-family: "PT Sans", sans-serif; font-size: 15px; color: var(--green-note); padding-top: 6px; }

  .social-row { left: 245px; top: 1105px; display: flex; gap: 14px; }
  .social-dot { width: 66px; height: 66px; border-radius: 50%; box-shadow: 0 3px 4px rgba(0,0,0,.2); }
</style>
</head>
<body>
  <svg width="0" height="0" style="position:absolute">
    <symbol id="spark" viewBox="0 0 34 34">
      <g stroke="#ffffff" stroke-width="3" stroke-linecap="round">
        <line x1="17" y1="4" x2="17" y2="30"/><line x1="4" y1="17" x2="30" y2="17"/>
        <line x1="8" y1="8" x2="26" y2="26"/><line x1="26" y1="8" x2="8" y2="26"/>
      </g>
      <circle cx="17" cy="17" r="4" fill="#8fc322"/>
    </symbol>
  </svg>

  <header>
    <div class="abs brand"><span class="brand-mark"></span><span class="brand-name">Loomcrest</span></div>
    <div class="abs brand-rule"></div>
    <h1 class="abs tagline">Plataforma de Saúde Pessoal</h1>
  </header>

  <main>
    <div class="abs social-signup"><span class="network-tab"></span><span class="label">SIGN UP WTH FRIENDLINE</span></div>
    <div class="abs field" style="top:294px">Email Address</div>
    <div class="abs field" style="top:358px">Password</div>
    <div class="abs field" style="top:418px">Rewrite Password</div>
    <div class="abs terms"><span class="box"></span><span>I accept the <a href="#">Terms and Conditions</a></span></div>
    <div class="abs signup-button">SIGN UP</div>

    <nav>
      <div class="abs menu-pill" style="left:293px;top:619px;width:359px"><svg><use href="#spark"/></svg><span class="title">SOBRE</span><span class="note">A brief description of us</span></div>
      <div class="abs menu-pill" style="left:305px;top:696px;width:336px"><svg><use href="#spark"/></svg><span class="title">NOSSO TIME</span><span class="note">Our Time</span></div>
      <div class="abs menu-pill" style="left:203px;top:772px;width:539px"><svg><use href="#spark"/></svg><span class="title">TERMOS E CONDIÇÕES</span><span class="note">Terms &amp; Conditions</span></div>
      <div class="abs menu-pill" style="left:220px;top:848px;width:505px"><svg><use href="#spark"/></svg><span class="title">TRABALHE CONOSCO</span><span class="note">Work with Us</span></div>
      <div class="abs menu-pill" style="left:334px;top:925px;width:277px"><svg><use href="#spark"/></svg><span class="title">BLOG</span><span class="note">See Our Blog</span></div>
      <div class="abs menu-pill" style="left:279px;top:1001px;width:388px"><svg><use href="#spark"/></svg><span class="title">CONTATO</span><span class="note">&nbsp;Get in touch With Us</span></div>
    </nav>
  </main>

  <footer class="abs social-row">
    <span class="social-dot" style="background:#2f4f96"></span>
    <span class="social-dot" style="background:#3aa7e0"></span>
    <span class="social-dot" style="background:#f4f4f4"></span>
    <span class="social-dot" style="background:#4a9b3a"></span>
    <span class="social-dot" style="background:#1b86b8"></span>
    <span class="social-dot" style="background:#d8322c"></span>
  </footer>
</body>
</html>
```